Ad Design for a child care centre

Bright Pebbles Child Care Centre offers a safe, nurturing environment where your child will get the attention and care that he or she needs. Our ratio of children to adults is always within state guidelines - and often even higher - to make certain each child receives top-quality care
We are also state licensed as a Child Care facility and have met or exceeded all health and safety guidelines.
3-5 year Kinder Funded Program
Story Time
Show and Tell
Puzzles and Games
Computer Time
Arts and Crafts
Music
Pre-Reading Activities
And much more
You can rest assured that your child will be cared for with the most kindness, love and respect. We believe all children are precious gifts and we treat them as though they are our own.
Full-time, part-time, Half days, Before, after-school schedules are available.
To learn more, contact us today! 03 9514 -0817 or info@brightpebbles.example.au

```html
<!DOCTYPE html>
<html lang="en">
<head>
<meta charset="utf-8">
<title>Bright Pebbles Child Care Centre</title>
<link href="https://fonts.googleapis.com/css2?family=Lora:wght@400;700&family=Libre+Baskerville:wght@700&family=Arimo:wght@400;700&display=swap" rel="stylesheet">
<style>
:root{
  --bg-top:#c9d4e6;
  --bg-mid:#eef1f7;
  --bg-bottom:#dfe5f0;
  --navy:#1b2550;
  --ink:#2a2f45;
  --orange:#f0811f;
  --panel:#4a7fd1;
  --panel-dark:#2f5fb0;
  --red:#d4201c;
  --yellow:#ffe23a;
  --white:#ffffff;
}
*{margin:0;padding:0;box-sizing:border-box}
html,body{width:849px;height:1200px;overflow:hidden}
body{
  position:relative;
  background:linear-gradient(180deg,var(--bg-top) 0,var(--bg-mid) 260px,var(--bg-mid) 880px,var(--bg-bottom) 1200px);
  font-family:'Arimo',sans-serif;
  color:var(--ink);
}
.brand{position:absolute;top:22px;left:0;width:100%;text-align:center}
.brand-name{
  font-family:'Lora',serif;font-weight:700;font-size:80px;line-height:1;
  color:var(--orange);letter-spacing:1px;
}
.brand-sub{
  font-family:'Libre Baskerville',serif;font-weight:700;font-size:48px;
  color:var(--navy);margin-top:12px;line-height:1;
}
.intro{
  position:absolute;top:186px;left:40px;width:769px;
  text-align:center;font-size:15px;line-height:1.45;color:var(--ink);
}
.gallery{
  position:absolute;top:270px;left:30px;width:789px;height:286px;
  background:linear-gradient(180deg,var(--panel),var(--panel-dark));
  border-radius:14px;box-shadow:0 4px 10px rgba(0,0,0,.25);
}
.photo{position:absolute;border:3px solid var(--white);border-radius:4px}
.photo-main{left:18px;top:18px;width:236px;height:250px;background:linear-gradient(135deg,#ecc1b1,#c08f82 55%,#6d5a63)}
.photo-grid{position:absolute;left:272px;top:18px;width:500px;height:250px;
  display:grid;grid-template-columns:repeat(5,1fr);grid-template-rows:1fr 1fr;gap:8px}
.photo-grid .photo{position:static}
.t1{background:linear-gradient(160deg,#d9a98f,#8a6a5c)}
.t2{background:linear-gradient(160deg,#b7c4d6,#6f7fa0)}
.t3{background:linear-gradient(160deg,#c98b72,#5e4a44)}
.t4{background:linear-gradient(160deg,#9fb06d,#5d6a3e)}
.t5{background:linear-gradient(160deg,#e0b48a,#a05d4a)}
.t6{background:linear-gradient(160deg,#8a6f5d,#3e3330)}
.t7{background:linear-gradient(160deg,#e6bfa5,#a67a6a)}
.t8{background:linear-gradient(160deg,#d48a6a,#7a4b3f)}
.t9{background:linear-gradient(160deg,#c7a3b8,#7d5a72)}
.t10{background:linear-gradient(160deg,#e2b29a,#9a6b5b)}
.licence{
  position:absolute;top:572px;left:150px;width:549px;text-align:center;
  font-size:15px;line-height:1.45;
}
.program-title{
  position:absolute;top:624px;left:168px;
  font-family:'Libre Baskerville',serif;font-weight:700;font-size:28px;color:var(--navy);
}
.activities{
  position:absolute;top:670px;left:170px;width:480px;
  display:grid;grid-template-columns:270px 210px;row-gap:3px;
  list-style:none;font-family:'Lora',serif;font-variant:small-caps;font-weight:700;
  font-size:18px;line-height:22px;color:var(--navy);
}
.offer{position:absolute;top:630px;left:682px;width:140px;height:130px}
.offer-text{
  position:absolute;top:0;left:0;width:100%;height:100%;
  display:flex;flex-direction:column;align-items:center;justify-content:center;
  color:var(--white);font-family:'Lora',serif;font-weight:700;text-align:center;transform:rotate(-8deg);
}
.offer-small{font-size:14px;letter-spacing:.5px}
.offer-big{font-size:34px;line-height:1}
.promise{
  position:absolute;top:786px;left:40px;width:769px;text-align:center;
  font-size:15px;line-height:1.45;
}
.schedule{
  position:absolute;top:843px;left:0;width:849px;height:50px;background:var(--red);
  display:flex;align-items:center;justify-content:center;
  color:var(--yellow);font-weight:700;font-size:21px;
}
.contact{position:absolute;top:913px;left:0;width:100%;height:80px}
.contact-lead{position:absolute;left:120px;top:0;font-size:15px}
.contact-phone{position:absolute;left:112px;top:20px;font-family:'Arimo',sans-serif;font-weight:700;font-size:42px;color:var(--navy)}
.contact-or{position:absolute;left:500px;top:32px;font-size:18px}
.contact-email{
  position:absolute;left:538px;top:26px;padding:6px 14px;
  background:var(--white);border:2px solid var(--red);border-radius:22px;
  font-weight:700;font-size:17px;color:var(--navy);
}
.website{
  position:absolute;top:998px;left:0;width:100%;text-align:center;
  font-family:'Libre Baskerville',serif;font-weight:700;font-size:32px;color:var(--navy);
}
</style>
</head>
<body>
<header class="brand">
  <div class="brand-name">Bright Pebbles</div>
  <div class="brand-sub">Child Care Centre</div>
</header>

<p class="intro">offers a safe, nurturing environment where your child will get the attention and care that he or she needs. Our ratio of children to adults is always within state guidelines - and often even higher - to make certain each child receives top-quality care</p>

<section class="gallery">
  <div class="photo photo-main" role="img" aria-label="Photo of a toddler at the centre"></div>
  <div class="photo-grid">
    <div class="photo t1" role="img" aria-label="Photo of children playing"></div>
    <div class="photo t2" role="img" aria-label="Photo of a child at an activity"></div>
    <div class="photo t3" role="img" aria-label="Photo of a child indoors"></div>
    <div class="photo t4" role="img" aria-label="Photo of a child outdoors"></div>
    <div class="photo t5" role="img" aria-label="Photo of children at play"></div>
    <div class="photo t6" role="img" aria-label="Photo of a child with toys"></div>
    <div class="photo t7" role="img" aria-label="Photo of a smiling child"></div>
    <div class="photo t8" role="img" aria-label="Photo of a child at craft time"></div>
    <div class="photo t9" role="img" aria-label="Photo of a child at the centre"></div>
    <div class="photo t10" role="img" aria-label="Photo of a child reading"></div>
  </div>
</section>

<p class="licence">We are also state licensed as a Child Care facility and have met or exceeded all health and safety guidelines.</p>

<h2 class="program-title">3-5 year Kinder Funded Program</h2>
<ul class="activities">
  <li>Story Time</li><li>Arts and Crafts</li>
  <li>Show and Tell</li><li>Music</li>
  <li>Puzzles and Games</li><li>Pre-Reading Activities</li>
  <li>Computer Time</li><li>And much more</li>
</ul>

<div class="offer">
  <svg width="140" height="130" viewBox="0 0 140 130">
    <polygon fill="#d4201c" points="70,2 80,20 99,8 102,30 124,26 116,47 138,56 118,68 132,86 110,90 114,112 93,104 84,126 70,110 56,126 47,104 26,112 30,90 8,86 22,68 2,56 24,47 16,26 38,30 41,8 60,20"/>
  </svg>
  <div class="offer-text"><span class="offer-small">FIRST MONTH</span><span class="offer-big">FREE</span></div>
</div>

<p class="promise">You can rest assured that your child will be cared for with the most kindness, love and respect.<br>We believe all children are precious gifts and we treat them as though they are our own.</p>

<div class="schedule">Full-time, Part-time, Half days, Before, After-School schedules are available.</div>

<section class="contact">
  <div class="contact-lead">To learn more, contact us today!</div>
  <div class="contact-phone">03 9514 -0817</div>
  <div class="contact-or">or</div>
  <div class="contact-email">info@brightpebbles.example.au</div>
</section>

<div class="website">www.brightpebbleschildcare.example.au</div>
</body>
</html>
```